Portal Panel Medic need professional looking business card printed on plastic, Commericial, Industri

We are family owned and operated garage door company in Indianapolis, Indiana. We sale service and install dock equipment, doors, operators. We are looking to expand our commercial/ industrial division. We also service all residential doors and operators. We are looking for a business that stands out of the crowd. We are committed to have the best customer service in the industry.

Target Market(s)

National and local general contractors, National/ Corpate service accounts,

Industry/Entity Type

Business Service

Contact Information for Business Card

To be printed on plastic stock

Font styles to use
Sans Serif

Colors
ffffff
f04a50
ec1f27

Requirements
Must have
• Name, website,email, phone number, position.
Nice to have
• A standout professional design

```html
<!DOCTYPE html>
<html lang="en">
<head>
<meta charset="utf-8">
<title>Portal Panel Medic – Business Card</title>
<link rel="stylesheet" href="https://fonts.googleapis.com/css2?family=Teko:wght@500&family=Fira+Sans:wght@400;600&display=swap">
<style>
  :root {
    --backdrop: #2a2a2a;
    --card: #e6e6e7;
    --red: #ec1f27;
    --red-soft: #f04a50;
    --ink: #3a3a3a;
  }
  * { margin: 0; padding: 0; box-sizing: border-box; }
  html, body {
    width: 1200px; height: 896px; overflow: hidden;
    background: var(--backdrop);
  }
  .canvas { position: relative; width: 1200px; height: 896px; }
  .card {
    position: absolute;
    width: 486px; height: 277px;
    background: var(--card);
    border-radius: 18px;
    box-shadow: 0 10px 24px rgba(0,0,0,0.45);
  }
  .card-front { left: 354px; top: 162px; }
  .card-back { left: 352px; top: 469px; }

  .brand {
    position: absolute; left: 0; right: 0; top: 124px;
    display: flex; justify-content: center; align-items: center; gap: 10px;
  }
  .brand-mark {
    width: 14px; height: 14px; background: var(--red); flex: none;
  }
  .brand-name {
    font-family: "Fira Sans", sans-serif; font-weight: 600;
    font-size: 24px; line-height: 28px;
    color: var(--red);
  }
  .front-web {
    position: absolute; left: 0; right: 0; top: 238px;
    text-align: center;
    font-family: "Fira Sans", sans-serif; font-size: 12px;
    color: var(--red);
  }

  .person {
    position: absolute; right: 269px; top: 116px;
    text-align: right;
  }
  .person-name {
    font-family: "Teko", sans-serif; font-weight: 500;
    font-size: 24px; line-height: 22px; letter-spacing: 0.5px;
    color: var(--red); text-transform: uppercase;
  }
  .person-role {
    font-family: "Fira Sans", sans-serif; font-size: 11px;
    color: var(--ink); margin-top: 4px;
  }
  .divider {
    position: absolute; left: 228px; top: 119px;
    width: 1px; height: 40px; background: var(--red);
  }
  .contact-list {
    position: absolute; left: 236px; top: 118px;
    list-style: none;
    font-family: "Fira Sans", sans-serif; font-size: 11px;
    line-height: 13.5px; color: var(--ink);
  }
  .contact-list li { display: flex; align-items: center; gap: 5px; }
  .contact-list svg { width: 9px; height: 9px; fill: var(--red); flex: none; }
  .address {
    position: absolute; left: 0; right: 0; top: 241px;
    text-align: center;
    font-family: "Fira Sans", sans-serif; font-size: 11px;
    color: var(--ink);
  }
  .address-label { color: var(--red); }
</style>
</head>
<body>
<div class="canvas">
  <section class="card card-front">
    <div class="brand">
      <span class="brand-mark" aria-hidden="true"></span>
      <span class="brand-name">Portal Panel Medic</span>
    </div>
    <p class="front-web">www.portalpanelmedic.com</p>
  </section>

  <section class="card card-back">
    <div class="person">
      <p class="person-name">Marcelo Ferreira</p>
      <p class="person-role">Director</p>
    </div>
    <div class="divider"></div>
    <ul class="contact-list">
      <li>
        <svg viewBox="0 0 24 24" aria-hidden="true"><path d="M6.6 10.8a15.1 15.1 0 0 0 6.6 6.6l2.2-2.2c.3-.3.7-.4 1-.2 1.1.4 2.3.6 3.6.6.6 0 1 .4 1 1V20c0 .6-.4 1-1 1A17 17 0 0 1 3 4c0-.6.4-1 1-1h3.5c.6 0 1 .4 1 1 0 1.3.2 2.5.6 3.6.1.3 0 .7-.2 1z"/></svg>
        (555) 014-2273
      </li>
      <li>
        <svg viewBox="0 0 24 24" aria-hidden="true"><path d="M2 5h20v14H2z M2 5l10 8 10-8" stroke="#e6e6e7" stroke-width="2"/></svg>
        mferreira@portalpanelmedic.com
      </li>
      <li>
        <svg viewBox="0 0 24 24" aria-hidden="true"><path d="M14 2a8 8 0 1 1-5.3 14l-5 5-1.7-1.7 5-5A8 8 0 0 1 14 2zm0 3a5 5 0 1 0 0 10 5 5 0 0 0 0-10z"/></svg>
        www.portalpanelmedic.com
      </li>
    </ul>
    <p class="address"><span class="address-label">Address-</span> Street Name Avenue, Suite 100 State, Zip Code,Country</p>
  </section>
</div>
</body>
</html>
```